WP website design (Dorlen Group)

We need a wordpress design for an established auction and real estate company based in Kansas. The winning design will incorporate a professional color scheme with company logo in a clean layout with specified widgets. The design needs to consider that this will be developed on a responsive theme. Colors are blue and gray, with perhaps black or other as an accent/highlight color.

Must Have:
- Navigation:
1) Home 2) Auctions 3) Real Estate Listings 4) Rentals 5) Our Team 6) Services 7) Past Auctions 8) Testimonials 9) Contact Us

Page will have large slideshow, please use either image provided as the initial slide. Homepage will have auctions - as at http://brindlebidhouse.com/upcoming-auctions/. Home page will also have 2 calls to action: "NOTIFY ME OF UPCOMING AUCTIONS" (newsletter signup), and "I AM READY TO SELL. PLEASE CONTACT ME FOR A FREE CONSULTATION." with an email button.

Footer will have smaller company logo, credit card logo, and attached association logos and this contact info:
.(555) 318-7061: OFFICE
(555) 318-7095: FAX
dgroup@vrbx.com: email
Address: 718 N. Elm Ave., Johnson KS
Mailing Address: PO Box 927, Johnson, KS

Widgets:
1) email sign up 2) Social media (twitter, FB, linked-in, pinterest) 3) Mortgage calculator 4) testimonials blog

Nice to Have:
- demonstrate the drop-down menu styling, e.g. under Auctions
Auction Calendar
4 Key Auction Methods
Auction Benefits

Industry/Entity Type

Real Estate

Font styles to use
Sans Serif

Colors

Designer to choose colors to be used in the design.

Requirements
Must have
• - Navigation:

.(555) 318-7061: OFFICE
(555) 318-7095: FAX
dgroup@vrbx.com: email

Widgets:
Nice to have
• Nice to Have:
Auction Calendar
4 Key Auction Methods
Auction Benefits

```html
<!DOCTYPE html>
<html lang="en">
<head>
<meta charset="utf-8">
<title>Dorlen Group — Auctions &amp; Real Estate</title>
<link href="https://fonts.googleapis.com/css2?family=PT+Sans:wght@400;700&family=Arimo:wght@400;700&display=swap" rel="stylesheet">
<style>
:root{
  --blue:#26279a;
  --ink:#2b2b2b;
  --text:#333;
  --red:#d11a1a;
  --page:#efefef;
  --white:#fff;
  --line:#dcdcdc;
  --calc:#7ab4ee;
  --social-a:#3b5998;
  --social-b:#1e9ad6;
  --social-c:#c9202a;
  --social-d:#1a6fb0;
}
*{box-sizing:border-box;margin:0;padding:0}
html,body{width:960px;height:1200px;overflow:hidden}
body{position:relative;background:var(--page);font-family:"Arimo",Arial,sans-serif;color:var(--text)}
.abs{position:absolute}
.head-font{font-family:"PT Sans",Arial,sans-serif}

/* header */
.brand{left:84px;top:32px}
.brand-name{font-family:"PT Sans",Arial,sans-serif;font-size:30px;color:var(--blue);font-weight:400}
.social{left:600px;top:56px;display:flex;align-items:center;gap:6px}
.social-label{font-size:17px;color:#444;margin-right:6px}
.social-dot{width:32px;height:32px;border-radius:50%}

/* navigation */
.nav{left:0;top:110px;width:960px;height:36px;background:var(--blue);border-bottom:3px solid #000}
.nav::after{content:"";position:absolute;left:0;right:0;bottom:-6px;height:1px;background:#000}
.nav-item{position:absolute;top:10px;font-size:12px;color:var(--white);white-space:nowrap}
.nav-sep{position:absolute;top:8px;width:1px;height:20px;background:#5556c0}
.dropdown{left:147px;top:149px;width:134px;background:var(--ink)}
.dropdown div{height:22px;line-height:22px;padding-left:15px;font-size:10px;color:#fff;border-bottom:1px solid #444;white-space:nowrap}
.dropdown .on{background:var(--blue)}

/* main */
.main{left:82px;top:146px;width:795px;height:937px;background:var(--white)}
.hero{left:82px;top:157px;width:553px;height:233px;background:linear-gradient(180deg,#6aa9e0 0%,#a9cff0 45%,#7d8e6a 70%,#4f7a3a 100%)}
.signup{left:636px;top:157px;width:241px;height:233px;background:var(--ink);color:#fff}
.signup h2{position:absolute;left:24px;top:8px;font-size:21px;font-weight:700}
.signup .sub{position:absolute;left:25px;top:39px;font-size:10px;white-space:nowrap}
.signup label{position:absolute;left:26px;font-size:11px}
.signup .field{position:absolute;left:26px;width:183px;height:27px;background:linear-gradient(#fff,#ececec)}
.signup .btn{position:absolute;left:133px;top:190px;width:77px;height:27px;background:#111;border-radius:3px;font-size:13px;font-weight:700;text-align:center;line-height:27px}

.section-title{left:100px;top:413px;font-size:18px;font-weight:700;color:#444;letter-spacing:.3px}

/* auction cards */
.auction{width:500px;height:285px;background:var(--white);border:1px solid var(--line);box-shadow:0 0 2px rgba(0,0,0,.15)}
.auction-head{height:36px;background:var(--blue);color:#fff;font-size:14px;font-weight:700;padding:11px 0 0 16px;letter-spacing:.3px}
.panel{position:absolute;background:#f6f6f6;border:1px solid var(--line);border-radius:3px}
.thumb{left:15px;top:48px;width:70px;height:61px;background:#fff;padding:4px}
.thumb div{width:100%;height:100%;background:linear-gradient(180deg,#8fc0ea 0%,#d8d0c4 50%,#5d8c3f 100%)}
.links{left:15px;top:133px;width:89px;height:82px;background:#fff}
.links h4{margin:4px;height:24px;background:var(--blue);color:#fff;font-size:13px;padding:3px 0 0 8px;letter-spacing:.5px}
.links p{font-size:10.5px;font-weight:700;padding:5px 0 4px 8px;display:flex;align-items:center;gap:6px}
.info{left:113px;top:49px;width:365px;height:87px;padding:8px 6px;font-size:9.6px;line-height:14.4px;text-transform:uppercase}
.info .hl{color:var(--red);font-weight:700}
.info b{font-weight:700}
.live{left:113px;top:148px;width:365px;height:101px;padding:10px 6px;font-size:11px;line-height:14.4px}
.live a{color:var(--red);font-weight:700;text-decoration:underline}

/* sidebar */
.side-box{left:637px;width:217px;background:var(--white);border:1px solid var(--line)}
.side-title{left:637px;width:217px;height:27px;background:var(--ink);color:#fff;font-size:17px;font-weight:700;padding:3px 0 0 8px;letter-spacing:.3px}
.consult{left:637px;top:443px;width:217px;height:92px;background:var(--ink);color:#fff}
.consult h3{position:absolute;left:7px;top:5px;font-size:17px}
.consult p{position:absolute;left:10px;top:34px;font-size:9.5px}
.consult .email{position:absolute;left:7px;top:55px;width:182px;height:27px;background:#fff;color:#666;font-size:11px;padding:7px 0 0 6px}
.consult .go{position:absolute;left:153px;top:56px;width:35px;height:25px;background:#ccc;border:1px solid #999;color:#222;font-size:14px;text-align:center;line-height:24px}
.calc{left:652px;top:580px;width:187px;height:170px;background:var(--calc);border-right:3px solid #2b5d9a;overflow:hidden}
.calc-row{position:absolute;left:7px;font-family:"PT Sans",Arial,sans-serif;font-size:13px;color:#1a1a3a;white-space:nowrap}
.calc-field{position:absolute;height:24px;background:linear-gradient(#fff,#e6e6e6);font-size:11px;text-align:right;padding:5px 5px 0 0;border:1px solid #9ab}
.calc-check{position:absolute;font-size:8.5px;color:#1a1a3a;display:flex;align-items:center;gap:2px;top:118px;white-space:nowrap}
.calc-box{width:16px;height:16px;background:#eee;border:1px solid #888;border-radius:2px;flex:none}
.side-text{position:absolute;left:18px;font-size:10px;line-height:16px;color:#333;white-space:nowrap}
.more{position:absolute;right:32px;font-size:9px;font-weight:700;font-style:italic;color:#333}

/* footer */
.footer{left:0;top:1083px;width:960px;height:117px;background:var(--ink);color:#ccc;font-size:10px;line-height:14.5px}
.footer .contact{position:absolute;left:102px;top:17px}
.badge{position:absolute;background:#fff;border:1px solid #999}
.card-shape{position:absolute;border-radius:3px}
.foot-brand{position:absolute;left:712px;top:50px}
.foot-brand span{font-family:"PT Sans",Arial,sans-serif;font-size:22px;color:#ddd}
</style>
</head>
<body>

<header>
  <div class="abs brand"><span class="brand-name">Dorlen Group</span></div>
  <div class="abs social">
    <span class="social-label">Social Media:</span>
    <span class="social-dot" style="background:var(--social-a)" role="img" aria-label="Social network link"></span>
    <span class="social-dot" style="background:var(--social-b)" role="img" aria-label="Social network link"></span>
    <span class="social-dot" style="background:var(--social-c)" role="img" aria-label="Social network link"></span>
    <span class="social-dot" style="background:var(--social-d)" role="img" aria-label="Social network link"></span>
  </div>
</header>

<div class="abs main"></div>

<nav class="abs nav">
  <span class="nav-item" style="left:98px">Home</span><span class="nav-sep" style="left:146px"></span>
  <span class="nav-item" style="left:162px">Auctions</span><span class="nav-sep" style="left:225px"></span>
  <span class="nav-item" style="left:239px">Real Estate Listings</span><span class="nav-sep" style="left:353px"></span>
  <span class="nav-item" style="left:372px">Rentals</span><span class="nav-sep" style="left:432px"></span>
  <span class="nav-item" style="left:457px">Our Team</span><span class="nav-sep" style="left:528px"></span>
  <span class="nav-item" style="left:551px">Services</span><span class="nav-sep" style="left:614px"></span>
  <span class="nav-item" style="left:631px">Past Auctions</span><span class="nav-sep" style="left:710px"></span>
  <span class="nav-item" style="left:724px">Testimonials</span><span class="nav-sep" style="left:799px"></span>
  <span class="nav-item" style="left:812px">Contact Us</span>
</nav>

<div class="abs hero" role="img" aria-label="Slideshow photo of two suburban houses with garages under a blue sky"></div>

<div class="abs dropdown">
  <div>Land &amp; Recreation (5)</div>
  <div class="on">Commercial (6)</div>
  <div>Residential (7)</div>
  <div>Homes with Acreage (8)</div>
  <div>Oil &amp; Gas (9</div>
</div>

<section class="abs signup head-font">
  <h2>Email sign-up</h2>
  <p class="sub" style="font-family:Arimo,Arial,sans-serif">NOTIFY ME OF UPCOMING AUCTIONS</p>
  <label style="top:66px">Your Name</label>
  <div class="field" style="top:91px"></div>
  <label style="top:128px">Your Address</label>
  <div class="field" style="top:151px"></div>
  <div class="btn">Subscribe</div>
</section>

<h1 class="abs section-title head-font">Upcoming Auctions</h1>

<article class="abs auction" style="left:98px;top:443px">
  <div class="auction-head head-font">160± ACRES LAND NOBLE COUNTY, OK</div>
  <div class="panel thumb"><div role="img" aria-label="House with a for-sale sign"></div></div>
  <div class="panel info">BILLINGS AREA * CROP &amp; TIMBER<br><span class="hl">160± ACRES LAND NOBLE COUNTY</span><b>, OK ~ BILLINGS AREA * CROP &amp; TIMBER ~ EXCELLENT HUNTING</b><br>ABSOLUTE AUCTION<br>SELLER: THE REDBUD HERITAGE FOUNDATION OF OKLAHOMA</div>
  <div class="panel links"><h4 class="head-font">LINKS</h4>
    <p><svg width="16" height="8"><rect x="0" y="1" width="5" height="6" fill="#111"/><rect x="7" y="1" width="9" height="1.5" fill="#111"/><rect x="7" y="3.5" width="9" height="1.5" fill="#111"/><rect x="7" y="6" width="9" height="1.5" fill="#111"/></svg>Details</p>
    <p><svg width="16" height="14"><rect x="1" y="1" width="10" height="8" fill="none" stroke="#111" stroke-width="1.5"/><rect x="5" y="5" width="10" height="8" fill="#fff" stroke="#111" stroke-width="1.5"/></svg>Photos</p>
  </div>
  <div class="panel live"><b>LIVE ON-SITE AUCTION WITH ONLINE BIDDING</b><br>Begins:&nbsp; Tuesday, March 12, 2013 at 10:00 AM CDT<br><a>Click Here to Bid Online Now!</a><br><b>Location:</b>&nbsp; See Directions<br>United States Billings, OK 74630</div>
</article>

<article class="abs auction" style="left:99px;top:744px">
  <div class="auction-head head-font">160± ACRES LAND NOBLE COUNTY, OK</div>
  <div class="panel thumb"><div role="img" aria-label="House with a for-sale sign"></div></div>
  <div class="panel info">BILLINGS AREA * CROP &amp; TIMBER<br><span class="hl">160± ACRES LAND NOBLE COUNTY</span><b>, OK ~ BILLINGS AREA * CROP &amp; TIMBER ~ EXCELLENT HUNTING</b><br>ABSOLUTE AUCTION<br>SELLER: THE REDBUD HERITAGE FOUNDATION OF OKLAHOMA</div>
  <div class="panel links"><h4 class="head-font">LINKS</h4>
    <p><svg width="16" height="8"><rect x="0" y="1" width="5" height="6" fill="#111"/><rect x="7" y="1" width="9" height="1.5" fill="#111"/><rect x="7" y="3.5" width="9" height="1.5" fill="#111"/><rect x="7" y="6" width="9" height="1.5" fill="#111"/></svg>Details</p>
    <p><svg width="16" height="14"><rect x="1" y="1" width="10" height="8" fill="none" stroke="#111" stroke-width="1.5"/><rect x="5" y="5" width="10" height="8" fill="#fff" stroke="#111" stroke-width="1.5"/></svg>Photos</p>
  </div>
  <div class="panel live"><b>LIVE ON-SITE AUCTION WITH ONLINE BIDDING</b><br>Begins:&nbsp; Tuesday, March 12, 2013 at 10:00 AM CDT<br><a>Click Here to Bid Online Now!</a><br><b>Location:</b>&nbsp; See Directions<br>United States Billings, OK 74630</div>
</article>

<aside>
  <section class="abs consult">
    <h3 class="head-font">Free Consultaion</h3>
    <p>I AM READY TO SELL.</p>
    <div class="email">Enter your email</div>
    <div class="go">GO</div>
  </section>

  <div class="abs side-box" style="top:566px;height:196px"></div>
  <div class="abs side-title head-font" style="top:541px">Mortgage calculator</div>
  <div class="abs calc">
    <span class="calc-row" style="top:10px">Loan Amount</span><div class="calc-field" style="left:99px;top:3px;width:82px;border:2px solid #f08a3c">525000</div>
    <span class="calc-row" style="top:38px">Loan Term</span><div class="calc-field" style="left:116px;top:31px;width:65px">30</div>
    <span class="calc-row" style="top:66px">Interest Rate</span><div class="calc-field" style="left:124px;top:59px;width:57px">5.25</div>
    <span class="calc-row" style="top:94px">Closing Cost</span><div class="calc-field" style="left:105px;top:87px;width:76px">5250</div>
    <span class="calc-check" style="left:2px"><svg class="calc-box" viewBox="0 0 16 16"><path d="M3 8l3 4 7-9" stroke="#2a9a2a" stroke-width="2.5" fill="none"/></svg>Assess Refinance</span>
    <span class="calc-check" style="left:102px"><span class="calc-box"></span>Compare Loans</span>
    <span class="calc-row" style="top:150px">Current Balance</span><div class="calc-field" style="left:111px;top:143px;width:70px">498279</div>
  </div>

  <div class="abs side-box" style="top:804px;height:88px">
    <p class="side-text" style="top:18px">Great Land Auction Companies Make<br>All the Difference Great Land Auction</p>
    <span class="more" style="top:64px">More Details »</span>
  </div>
  <div class="abs side-title head-font" style="top:778px">Cients Testimonials</div>

  <div class="abs side-box" style="top:939px;height:89px">
    <p class="side-text" style="top:11px">Great Land Auction Companies Make<br>All the Difference Great Land Auction</p>
    <p class="side-text" style="top:46px">Great Land Auction Companies Make</p>
    <span class="more" style="top:68px">More Details »</span>
  </div>
  <div class="abs side-title head-font" style="top:913px;padding-left:12px">Auction Benefits</div>
</aside>

<footer class="abs footer">
  <div class="contact">
    OFFICE : (555) 318-7061<br>FAX : (555) 318-7095<br>Email : dgroup@vrbx.com<br><br style="line-height:7px">
    Address: 718 N. Elm Ave., Johnson KS<br>Mailing Address: PO Box 927, Johnson, KS
  </div>
  <span class="badge" style="left:338px;top:65px;width:30px;height:32px" role="img" aria-label="Auctioneers association badge"></span>
  <span class="badge" style="left:373px;top:65px;width:52px;height:32px" role="img" aria-label="State auctioneers association badge"></span>
  <span class="card-shape" style="left:445px;top:67px;width:48px;height:30px;background:#e8e8ee" role="img" aria-label="Accepted payment card"></span>
  <span class="card-shape" style="left:494px;top:67px;width:52px;height:30px;background:#d9823a" role="img" aria-label="Accepted payment card"></span>
  <span class="card-shape" style="left:550px;top:67px;width:47px;height:30px;background:#f0f0f0" role="img" aria-label="Accepted payment card"></span>
  <div class="foot-brand"><span>Dorlen Group</span></div>
</footer>

</body>
</html>
```